Cover Design Project for Book About Data and Opinion/Political Polling

Need a cover for a paperback book (and possibly ebook) about data and research, specifically public opinion polling.

The book is titled "Harbor of Echoes" and the subtitle is "How Lighthouse Keepers Charted the Northern Coast". It focuses on two core themes - the drivers behind why political polls are no longer reliable, and what it would take to fix that.

Something that screams "data" or "information", appeals to consumers of public opinion polls, and is colorful with a fair amount of red and blue, would be ideal. Preferably something graphical that implies worsening quality

Its 6x9 trim and at 229 pages has a spine of approximately 0.516". Including bleed, the dimensions needed are roughly 12.77"x9.25"

The lower left corner of the back cover should be free of content so the barcode can be placed there.

Some content attached.

Target Market(s)

Consumers of opinion polls
Pollsters/Polling Organizations
High-Net Worth Individuals

Font styles to use
Serif

Colors
0355a3
ec1f27

Requirements
Must have
• Red and Blue colors
• Imagery that tells potential readers the contents are data-oriented but consumable by people regardless of their data/tech literacy
Nice to have
• More color than just red and blue
Should not have
• Any sort of political partisanship
• The long bio on the back cover (use the short one, the long one was only provided for context)

```html
<!DOCTYPE html>
<html lang="en">
<head>
<meta charset="utf-8">
<title>Harbor of Echoes — Cover Wrap</title>
<link rel="stylesheet" href="https://fonts.googleapis.com/css2?family=Bebas+Neue&family=Montserrat:wght@600;700&family=Roboto+Condensed:wght@700&family=Nunito+Sans:wght@400;700&display=swap">
<style>
  :root {
    --backdrop: #716e6f;
    --paper: #ffffff;
    --ink: #1b1b1b;
    --blue: #2364a1;
    --red: #b3080b;
    --photo-light: #f3f3f3;
    --photo-mid: #dcdcdc;
  }
  html, body {
    margin: 0;
    width: 1200px;
    height: 1200px;
    overflow: hidden;
    background: var(--backdrop);
  }
  .wrap {
    position: absolute;
    left: 48px;
    top: 198px;
    width: 1110px;
    height: 806px;
    background: var(--paper);
    overflow: hidden;
  }
  /* Back cover */
  .blurb {
    position: absolute;
    left: 78px;
    top: 80px;
    width: 383px;
    font-family: "Nunito Sans", sans-serif;
    font-size: 13.6px;
    line-height: 16.2px;
    color: var(--ink);
    text-align: justify;
    letter-spacing: -0.2px;
  }
  .blurb p { margin: 0 0 16px; }
  .blurb ul {
    margin: 0 0 16px;
    padding-left: 16px;
    text-align: left;
    width: 340px;
  }
  .blurb li { padding-left: 0; }
  .bio-band {
    position: absolute;
    left: 0;
    top: 529px;
    width: 538px;
    height: 159px;
    background: var(--red);
  }
  .author-photo {
    position: absolute;
    left: 20px;
    top: 492px;
    width: 144px;
    height: 196px;
    background: linear-gradient(180deg, #c7c1bd 0%, #3c4a63 45%, #26324a 100%);
    border-radius: 60px 60px 0 0;
  }
  .bio {
    position: absolute;
    left: 182px;
    top: 559px;
    width: 324px;
    margin: 0;
    font-family: "Nunito Sans", sans-serif;
    font-size: 12.8px;
    line-height: 15px;
    color: #fff;
    text-align: justify;
    letter-spacing: -0.3px;
  }
  .bio strong { font-weight: 700; }
  /* Spine */
  .spine-title, .spine-author {
    position: absolute;
    writing-mode: vertical-rl;
    font-family: "Montserrat", sans-serif;
    font-weight: 700;
    white-space: nowrap;
  }
  .spine-title {
    left: 544px;
    top: 144px;
    font-size: 24px;
    color: var(--blue);
  }
  .spine-title .accent { color: var(--red); }
  .spine-author {
    left: 548px;
    top: 490px;
    font-size: 17px;
    font-weight: 600;
    color: var(--blue);
  }
  /* Front cover */
  .cover-art {
    position: absolute;
    left: 576px;
    top: 0;
    width: 534px;
    height: 300px;
    background: linear-gradient(160deg, var(--paper) 0%, var(--photo-light) 45%, var(--photo-mid) 70%, #e4b9b4 100%);
  }
  .title-main {
    position: absolute;
    left: 576px;
    width: 534px;
    top: 262px;
    margin: 0;
    text-align: center;
    font-family: "Bebas Neue", sans-serif;
    font-weight: 400;
    font-size: 176px;
    line-height: 1;
    color: var(--blue);
    padding-left: 48px;
    box-sizing: border-box;
  }
  .title-main .line-2 {
    display: block;
    margin-top: -8px;
    font-family: "Montserrat", sans-serif;
    font-weight: 700;
    font-size: 60px;
    letter-spacing: -1.5px;
    color: var(--red);
  }
  .rule {
    position: absolute;
    left: 656px;
    width: 396px;
    height: 3px;
    background: var(--blue);
  }
  .rule.top { top: 603px; }
  .rule.bottom { top: 689px; }
  .subtitle {
    position: absolute;
    left: 656px;
    top: 618px;
    width: 396px;
    margin: 0;
    text-align: center;
    font-family: "Montserrat", sans-serif;
    font-weight: 700;
    font-size: 17px;
    line-height: 30px;
    color: var(--red);
    letter-spacing: 0.3px;
  }
  .front-author {
    position: absolute;
    left: 656px;
    top: 730px;
    width: 396px;
    margin: 0;
    text-align: center;
    font-family: "Roboto Condensed", sans-serif;
    font-weight: 700;
    font-size: 38px;
    color: var(--blue);
  }
</style>
</head>
<body>
  <main class="wrap">
    <section class="back-cover">
      <div class="blurb">
        <p>You may have noticed that a lot of opinion polls aren’t very reliable. For a long time this wasn’t so true, and pollsters have been coasting on former reputations of accuracy, but it’s getting much harder for them to do so.</p>
        <p>Conditions used to be such that polls could largely compensate for many of the issues that plague the social sciences. Polling firms built business models which assumed these conditions as given. However, since the dawn of the new millennium, those assumptions have been breaking down, imperiling the industry. Harbor of Echoes explains:</p>
        <ul>
          <li>How social and technological changes contribute to growing polling inaccuracy</li>
          <li>Why survey research is a format predisposed to getting things wrong</li>
          <li>The reasons why traditional formats are unlikely to get any better</li>
          <li>What changes are needed in order for findings to reflect reality</li>
        </ul>
        <p>Fixing the problems isn’t easy, but it can be done. If you want to better understand the scope of the issues and what it would take to right the ship, this book is for you.</p>
      </div>
      <div class="bio-band"></div>
      <div class="author-photo" role="img" aria-label="Portrait photo of the author in a dark shirt and tie"></div>
      <p class="bio"><strong>Martin Hale</strong> holds a BA and MA in Political Science from Lakemont University and has conducted research for multiple advocacy groups, synthesizing the findings into reports cited by national news outlets as well as being used to make policy. He continues to provide his expertise on data and research as a consultant while building his company.</p>
    </section>

    <section class="spine">
      <div class="spine-title">HARBOR <span class="accent">OF ECHOES</span></div>
      <div class="spine-author">MARTIN HALE, BA.,MA</div>
    </section>

    <section class="front-cover">
      <div class="cover-art" role="img" aria-label="Photo of a red pencil ticking boxes on a survey checklist"></div>
      <h1 class="title-main">HARBOR<span class="line-2">OF ECHOES</span></h1>
      <div class="rule top"></div>
      <p class="subtitle">HOW LIGHTHOUSE KEEPERS<br>CHARTED THE NORTHERN COAST</p>
      <div class="rule bottom"></div>
      <p class="front-author">MARTIN HALE, BA.,MA</p>
    </section>
  </main>
</body>
</html>
```